Company website for an international IT business

We require a website for our business, Corvell Solutions. The business has two primary areas: Horizons, which includes two machine learning/deep learning based products and IT consultancy, which is the service we provide to other businesses.

We bridge cutting-edge research to market.

STYLING:
The site can be on single page or multi-page. This is fully open to suggestion. So long as the look and feel are consistent. Currently, we have no strong preference for colors, styles or layouts.
You can find the logo of our website in the attachment “Corvell-logo.png” and “Corvell-logo-landscape.png”.

CONTENT:
You can find the text of the website in “Website-Content.pdf”, which explains the services and products of our business. The format of the text is also open to suggestion - including breaking up the text into visually appealing sections.
We would also like to include suitable images on the website so that it does not appear to be a text-heavy page. We are happy to have placeholder images on stock image sites if needed. We are open to suggestions on placing of images

ATTACHMENT:

Industry/Entity Type

It Company

Coding

Coded - Design and coding required

Number of Pages Required

1 page

Colors

Designer to choose colors to be used in the design.

Requirements
Must have
• A full description of the requirement is in the attachment "Website-Content.pdf"
• The design must have HTML/CSS, and all resources relevant (images, fonts etc)
• We are
Nice to have
• We are open to suggestions on top of the requirement, please reach out and communicate.

```html
<!DOCTYPE html>
<html lang="en">
<head>
<meta charset="utf-8">
<title>Corvell Solutions</title>
<link href="https://fonts.googleapis.com/css2?family=Roboto:wght@300;400;500;700;900&display=swap" rel="stylesheet">
<style>
:root{
  --blue:#1b75bc;
  --blue-dark:#0f4f86;
  --orange:#f7941d;
  --ink:#2a2a2a;
  --muted:#6d6d6d;
  --dark:#262626;
  --footer:#f4f4f4;
  --rule:#dcdcdc;
  --white:#ffffff;
}
*{box-sizing:border-box;margin:0;padding:0}
html,body{width:1200px;height:2940px;overflow:hidden}
body{font-family:"Roboto",Arial,sans-serif;color:var(--ink);background:var(--white)}
.section-title{font-size:42px;font-weight:700;text-align:center;letter-spacing:1px;color:var(--ink)}
.section-intro{font-size:17px;line-height:26px;color:var(--muted);text-align:center;width:760px;margin:18px auto 0}

/* Hero */
.hero{position:relative;height:608px;overflow:hidden}
.hero-photo{position:absolute;inset:0;background:linear-gradient(135deg,#3d4e60 0%,#1f2c3a 45%,#475868 75%,#2b3846 100%)}
.hero-shade{position:absolute;inset:0;background:rgba(10,20,35,.45)}
.nav{position:relative;display:flex;align-items:center;justify-content:space-between;padding:20px 100px 0}
.brand{display:flex;align-items:center;gap:14px}
.brand-mark{width:64px;height:64px;border-radius:50%;background:var(--blue)}
.brand-name{font-size:40px;font-weight:700;color:var(--white);letter-spacing:2px}
.menu{display:flex;align-items:center;gap:30px;list-style:none}
.menu a{color:var(--white);text-decoration:none;font-size:15px;font-weight:500}
.menu .login{border:2px solid var(--blue);background:var(--blue);padding:8px 18px}
.hero-copy{position:relative;text-align:center;margin-top:150px;color:var(--white)}
.hero-copy h1{font-size:64px;font-weight:700;letter-spacing:2px}
.hero-copy p{font-size:18px;line-height:27px;width:640px;margin:14px auto 0}
.btn{display:inline-block;background:var(--blue);color:var(--white);font-size:17px;font-weight:500;padding:13px 26px;margin-top:28px;text-decoration:none}

/* Horizons */
.horizons{padding:68px 0 0;height:1188px - 608px}
.horizons{height:580px}
.product-cards{display:flex;width:1000px;margin:50px auto 0}
.product-card{width:500px;height:300px;display:flex;flex-direction:column;align-items:center;justify-content:center;color:var(--white);text-align:center;padding:0 60px}
.product-card.lumen{background:linear-gradient(135deg,#2a8fd8,var(--blue))}
.product-card.quarry{background:linear-gradient(135deg,#f9a23a,var(--orange))}
.product-card svg{width:84px;height:84px}
.product-card h3{font-size:26px;font-weight:700;letter-spacing:1px;margin-top:14px}
.product-card p{font-size:15px;line-height:23px;margin-top:10px}

/* About */
.about{display:flex;height:452px}
.about-copy{width:600px;background:linear-gradient(135deg,#2b88d1,var(--blue-dark));color:var(--white);padding:80px 60px 0 100px}
.about-copy h2{font-size:50px;font-weight:700;letter-spacing:1px}
.about-copy p{font-size:15px;line-height:24px;margin-top:20px}
.btn-outline{display:inline-block;border:2px solid var(--white);color:var(--white);font-size:13px;font-weight:700;padding:8px 16px;margin-top:26px;text-decoration:none}
.about-photo{width:600px;background:linear-gradient(135deg,#e6e6e6,#8d8d8d 55%,#3a3a3a)}

/* Consultancy */
.consultancy{padding:60px 0 0;height:608px}
.services{display:flex;justify-content:space-between;width:1000px;margin:70px auto 0}
.service{width:300px;position:relative}
.service-photo{height:180px}
.service:nth-child(1) .service-photo{background:linear-gradient(135deg,#c9b59a,#7a6a58)}
.service:nth-child(2) .service-photo{background:linear-gradient(135deg,#3e5a78,#1d2a3a)}
.service:nth-child(3) .service-photo{background:linear-gradient(135deg,#3270b8,#142d55)}
.service-badge{position:absolute;top:-36px;left:0;width:96px;height:96px;border-radius:50%;background:var(--white);border:3px solid var(--blue);display:flex;align-items:center;justify-content:center}
.service-badge svg{width:46px;height:46px}
.service h3{font-size:24px;font-weight:500;margin-top:22px}
.service p{font-size:15px;line-height:23px;color:var(--muted);margin-top:10px}

/* Testimonial */
.testimonial{position:relative;height:272px;background:linear-gradient(135deg,#3b3b3b,var(--dark));color:var(--white);display:flex;align-items:center;padding:0 100px}
.client-photo{width:120px;height:120px;border-radius:50%;background:linear-gradient(135deg,#d9c3a8,#6b5a48);border:4px solid var(--white);flex:none}
.quote{margin-left:40px;width:820px}
.quote p{font-size:16px;line-height:25px;font-style:italic}
.quote cite{display:block;font-style:normal;font-weight:700;font-size:16px;margin-top:14px}
.quote-mark{position:absolute;right:110px;bottom:70px;width:48px;height:40px}

/* Footer */
.footer{background:var(--footer);height:360px;display:flex;padding:60px 100px 0;gap:60px}
.footer-brand{width:250px}
.footer-brand .brand-name{color:var(--ink);font-size:34px}
.footer-brand .brand-mark{width:56px;height:56px}
.social{display:flex;gap:10px;margin-top:18px;margin-left:70px}
.social span{width:26px;height:26px;border-radius:50%;background:var(--ink)}
.footer-col h4{font-size:20px;font-weight:700;letter-spacing:1px;margin-bottom:22px}
.newsletter{width:250px}
.newsletter p{font-size:14px;line-height:21px;color:var(--muted)}
.newsletter .field{width:230px;height:38px;border:1px solid var(--rule);background:var(--white);margin-top:18px;font-size:13px;color:#999;padding:10px 12px}
.newsletter .subscribe{display:inline-block;background:var(--blue);color:var(--white);font-size:13px;font-weight:700;padding:10px 16px;margin-top:14px}
.contact{width:250px}
.contact li{list-style:none;display:flex;gap:12px;font-size:14px;line-height:21px;color:var(--muted);margin-bottom:16px}
.contact svg{width:18px;height:18px;flex:none;margin-top:2px}
.links li{list-style:none;font-size:14px;color:var(--muted);margin-bottom:11px}
.copyright{height:60px;background:#e9e9e9;border-top:1px solid var(--rule);display:flex;align-items:center;justify-content:center;font-size:13px;color:var(--muted)}
</style>
</head>
<body>

<header class="hero">
  <div class="hero-photo" role="img" aria-label="Photo of an operations room with people working at computer screens"></div>
  <div class="hero-shade"></div>
  <nav class="nav">
    <div class="brand"><span class="brand-mark"></span><span class="brand-name">CORVELL</span></div>
    <ul class="menu">
      <li><a href="#">HOME</a></li>
      <li><a href="#">HORIZONS</a></li>
      <li><a href="#">IT CONSULTANCY</a></li>
      <li><a href="#">ABOUT</a></li>
      <li><a href="#">CONTACT US</a></li>
      <li><a class="login" href="#">LOGIN</a></li>
    </ul>
  </nav>
  <div class="hero-copy">
    <h1>CORVELL SOLUTIONS</h1>
    <p>We bridge cutting-edge research to market, turning new ideas in machine learning into products and services that help businesses grow.</p>
    <a class="btn" href="#">Read More</a>
  </div>
</header>

<section class="horizons">
  <h2 class="section-title">CORVELL HORIZONS</h2>
  <p class="section-intro">Horizons is our product line: two machine learning and deep learning tools built from current research and shaped for daily use by real teams.</p>
  <div class="product-cards">
    <div class="product-card lumen">
      <svg viewBox="0 0 84 84" fill="none" stroke="#fff" stroke-width="4"><rect x="20" y="20" width="44" height="44" rx="4"/><rect x="32" y="32" width="20" height="20"/><path d="M30 12v8M42 12v8M54 12v8M30 64v8M42 64v8M54 64v8M12 30h8M12 42h8M12 54h8M64 30h8M64 42h8M64 54h8"/></svg>
      <h3>LUMEN</h3>
      <p>A deep learning engine that reads your data and surfaces patterns, forecasts and clear answers in minutes.</p>
    </div>
    <div class="product-card quarry">
      <svg viewBox="0 0 84 84" fill="none" stroke="#fff" stroke-width="4"><rect x="10" y="14" width="64" height="42" rx="3"/><path d="M42 56v12M28 70h28"/><path d="M22 44l10-10 8 8 14-14 8 8"/></svg>
      <h3>QUARRYLENS</h3>
      <p>A smart search tool that helps teams explore large archives and find the right record quickly.</p>
    </div>
  </div>
</section>

<section class="about">
  <div class="about-copy">
    <h2>ABOUT CORVELL</h2>
    <p>Corvell Solutions is an international IT business founded by engineers and researchers. We take ideas from the lab and shape them into tools that work in the real world. Our team builds machine learning products, advises clients on software and systems, and supports them from the first plan to the final launch. We value plain talk, careful work and long partnerships with every client we serve.</p>
    <a class="btn-outline" href="#">READ MORE</a>
  </div>
  <div class="about-photo" role="img" aria-label="Photo of business people in silhouette against a bright office window"></div>
</section>

<section class="consultancy">
  <h2 class="section-title">IT CONSULTANCY</h2>
  <p class="section-intro">Corvell Solutions is an IT consultancy firm with a difference. We can provide IT expertise for your business at any stage, from initial idea to live systems.</p>
  <div class="services">
    <div class="service">
      <div class="service-photo" role="img" aria-label="Photo of a team planning software on a desk"></div>
      <div class="service-badge"><svg viewBox="0 0 46 46" fill="none" stroke="#1b75bc" stroke-width="3"><path d="M16 14L6 23l10 9M30 14l10 9-10 9M26 10l-6 26"/></svg></div>
      <h3>Software development</h3>
      <p>Custom software planned, built and tested with you, from small tools to full business platforms.</p>
    </div>
    <div class="service">
      <div class="service-photo" role="img" aria-label="Photo of connected devices and a control screen"></div>
      <div class="service-badge"><svg viewBox="0 0 46 46" fill="none" stroke="#1b75bc" stroke-width="3"><circle cx="23" cy="23" r="5"/><circle cx="8" cy="10" r="4"/><circle cx="38" cy="10" r="4"/><circle cx="23" cy="40" r="4"/><path d="M11 13l8 6M35 13l-8 6M23 28v8"/></svg></div>
      <h3>IOT System Design</h3>
      <p>Connected device systems designed to be secure, reliable and simple to manage at any scale.</p>
    </div>
    <div class="service">
      <div class="service-photo" role="img" aria-label="Photo of a blue digital network graphic"></div>
      <div class="service-badge"><svg viewBox="0 0 46 46" fill="none" stroke="#1b75bc" stroke-width="3"><rect x="10" y="10" width="26" height="26" rx="3"/><rect x="18" y="18" width="10" height="10"/><path d="M17 4v6M29 4v6M17 36v6M29 36v6M4 17h6M4 29h6M36 17h6M36 29h6"/></svg></div>
      <h3>Machine learning solutions</h3>
      <p>Models trained on your own data to automate tasks, predict demand and guide better decisions.</p>
    </div>
  </div>
</section>

<section class="testimonial">
  <div class="client-photo" role="img" aria-label="Portrait photo of the client"></div>
  <blockquote class="quote">
    <p>"Corvell Solutions understood our goals from the very first meeting. Their team explained each step clearly, delivered on time and built a system our staff enjoy using every day. We now plan every new project with them and recommend them to our partners."</p>
    <cite>Daniel Reyes, Corvell Solutions</cite>
  </blockquote>
  <svg class="quote-mark" viewBox="0 0 48 40" fill="#fff"><path d="M0 40V22C0 10 6 3 18 0l2 5C13 8 10 12 10 18h10v22zM28 40V22c0-12 6-19 18-22l2 5c-7 3-10 7-10 13h10v22z"/></svg>
</section>

<footer>
  <div class="footer">
    <div class="footer-brand">
      <div class="brand"><span class="brand-mark"></span><span class="brand-name">CORVELL</span></div>
      <div class="social"><span></span><span></span><span></span><span></span></div>
    </div>
    <div class="footer-col newsletter">
      <h4>SIGN UP FOR NEWSLETTER</h4>
      <p>Get our latest news, product updates and research notes straight to your inbox.</p>
      <div class="field">Enter email</div>
      <span class="subscribe">SUBSCRIBE</span>
    </div>
    <div class="footer-col contact">
      <h4>CONTACT US</h4>
      <ul>
        <li><svg viewBox="0 0 18 18" fill="#6d6d6d"><path d="M9 0C5.5 0 3 2.6 3 6c0 4.5 6 12 6 12s6-7.5 6-12c0-3.4-2.5-6-6-6zm0 8.5A2.5 2.5 0 1 1 9 3.5a2.5 2.5 0 0 1 0 5z"/></svg><span>Corvell Solutions<br>118 Harbor Lane, Westbrook</span></li>
        <li><svg viewBox="0 0 18 18" fill="#6d6d6d"><path d="M4 1l3 4-2 2c1 2 3 4 5 5l2-2 4 3-2 4C7 16 2 11 1 3z"/></svg><span>Phone: (555) 014-2280</span></li>
        <li><svg viewBox="0 0 18 18" fill="none" stroke="#6d6d6d" stroke-width="1.6"><rect x="1" y="3" width="16" height="12"/><path d="M1 3l8 7 8-7"/></svg><span>Email: hello@corvellsolutions.example</span></li>
      </ul>
    </div>
    <div class="footer-col links">
      <h4>QUICK LINKS</h4>
      <ul>
        <li>Home</li><li>About</li><li>Horizons</li><li>Services</li><li>FAQ</li><li>Contact Us</li>
      </ul>
    </div>
  </div>
  <div class="copyright">© 2024 Corvell Solutions. All Rights Reserved.</div>
</footer>

</body>
</html>
```